Lawn maintenance
We are your green choice!
weekly , biweekly

Target Market(s)

lawn care

Industry/Entity Type

Lawn Care

Contact Information for Business Card

eye catching - not you normal "lawn business" card

Logo Text

Tall Oak Lawncare

Font styles to use
Serif
Sans Serif

Colors
ec1f27
00a990
9bcb3c
0455a3

Requirements
Must have
• Milo Hanford
• 410-555-0187
• Lawn maintenance
• We are your green choice!
• Call for a quote today!
• weekly or biweekly
Nice to have
• maybe some poker chips or playing cards
Should not have
• snow removal

```html
<!DOCTYPE html>
<html lang="en">
<head>
<meta charset="utf-8">
<title>Tall Oak Lawncare – Business Card</title>
<link rel="stylesheet" href="https://fonts.googleapis.com/css2?family=Lato:wght@400;700&display=swap">
<style>
  :root {
    --backdrop: #555555;
    --paper: #ffffff;
    --teal: #00a990;
    --lime: #9bcb3c;
    --lime-deep: #8ab834;
    --ink: #333333;
  }
  * { margin: 0; padding: 0; box-sizing: border-box; }
  html, body {
    width: 1200px;
    height: 900px;
    overflow: hidden;
    background: var(--backdrop);
    font-family: "Lato", Arial, sans-serif;
  }
  .stage { position: relative; width: 1200px; height: 900px; }
  .card {
    position: absolute;
    top: 170px;
    width: 347px;
    height: 561px;
    overflow: hidden;
  }
  .card--front { left: 259px; background: var(--paper); }
  .card--back {
    left: 631px;
    background: linear-gradient(180deg, var(--lime-deep) 0%, var(--lime-deep) 55%, var(--lime) 100%);
  }
  .brand-name {
    position: absolute;
    left: 0;
    width: 100%;
    text-align: center;
    font-weight: 700;
    font-size: 40px;
    line-height: 1.1;
    letter-spacing: 2px;
    text-transform: uppercase;
  }
  .card--front .brand-name { top: 130px; color: var(--teal); }
  .card--back .brand-name { top: 230px; color: var(--paper); }
  .contact-name {
    position: absolute;
    top: 298px;
    width: 100%;
    text-align: center;
    color: var(--teal);
    font-size: 24px;
    letter-spacing: 0.5px;
    text-transform: uppercase;
  }
  .contact-phone {
    position: absolute;
    top: 334px;
    width: 100%;
    text-align: center;
    color: var(--ink);
    font-size: 17px;
  }
  .contact-phone .label { color: var(--lime); }
  .band {
    position: absolute;
    left: 0;
    width: 100%;
    height: 70px;
    display: flex;
    flex-direction: column;
    justify-content: center;
    align-items: center;
    color: var(--paper);
    text-transform: uppercase;
    font-size: 15.5px;
    line-height: 1.4;
  }
  .band--tagline { top: 375px; background: var(--lime); }
  .band--offer { top: 457px; background: var(--teal); font-weight: 700; }
</style>
</head>
<body>
<main class="stage">
  <section class="card card--front">
    <h1 class="brand-name">Tall Oak Lawncare</h1>
    <p class="contact-name">Milo Hanford</p>
    <p class="contact-phone"><span class="label">P:</span> 410-555-0187</p>
    <div class="band band--tagline">
      <span>Lawn Maintenance</span>
      <span>We are your green choice!</span>
    </div>
    <div class="band band--offer">
      <span>Call for a quote today!</span>
      <span>Weekly or biweekly</span>
    </div>
  </section>
  <section class="card card--back">
    <h2 class="brand-name">Tall Oak Lawncare</h2>
  </section>
</main>
</body>
</html>
```